Cedar Hollow responsive web design

We need a responsive, bootstrap compatible (but design only - PSD files) website design for a fly fishing shop and guide service.

Design should be very clean. Home Page design + interior page design please.

Possible Home Page Content:
Slide Show
Highlight Three Features: Guided Trips, Fly Shop, Missouri River
About

Thank you and good luck!

Shop

• This will be used on Bootstrap CMS so needs 12 column bootstrap measurements.

DESIGN ONLY NEEDED (clean PSD files), no programming required.
Need a Home Page layout and secondary page layout

Must show use of the following:
H1 - H5 font uses
link color
Dropdown for navigation bar
Button example
• No cutout images, this will be part of CMS and client needs to be able to update most content without knowing photoshop.

```html
<!DOCTYPE html>
<html lang="en">
<head>
<meta charset="utf-8">
<title>Cedar Hollow — Fly Shop &amp; Guide Service</title>
<link href="https://fonts.googleapis.com/css2?family=Arimo:ital,wght@0,400;0,700;1,400&amp;display=swap" rel="stylesheet">
<style>
  :root {
    --sky: #5fb8d9;
    --sky-dark: #3a9cc2;
    --teal: #2a8596;
    --ink: #2b2b2b;
    --text: #666;
    --nav: #444;
    --panel: #f0f0f0;
    --footer: #555;
    --white: #fff;
  }
  * { box-sizing: border-box; margin: 0; padding: 0; }
  html, body { width: 970px; height: 1200px; overflow: hidden; }
  body { position: relative; background: var(--white); font-family: "Arimo", Arial, sans-serif; color: var(--text); }
  .abs { position: absolute; }

  .site-header { left: 0; top: 0; width: 970px; height: 82px; background: var(--white); }
  .header-rule { left: 0; top: 82px; width: 970px; height: 4px; background: var(--sky); z-index: 2; }
  .brand-plate { left: 138px; top: 40px; width: 146px; height: 70px; background: var(--white); border-radius: 0 0 73px 73px / 0 0 40px 40px; z-index: 3; }
  .brand { left: 142px; top: 10px; width: 120px; height: 70px; z-index: 4; display: flex; align-items: center; gap: 6px; }
  .brand-mark { width: 14px; height: 14px; background: var(--sky); flex: none; }
  .brand-name { font-size: 17px; font-weight: 700; color: var(--ink); line-height: 1.1; }

  .main-nav { top: 37px; font-size: 11px; color: var(--nav); text-transform: uppercase; letter-spacing: .1px; }

  .hero { left: 0; top: 86px; width: 970px; height: 392px; background: linear-gradient(100deg, #4a3f33 0%, #6e6a58 35%, #5c5a4c 55%, #2f4250 75%, #24343f 100%); }
  .hero-title { left: 628px; top: 150px; font-size: 52px; font-weight: 700; color: var(--white); line-height: 1; }
  .hero-tag { left: 638px; font-size: 16px; color: var(--white); text-transform: uppercase; }
  .hero-sub { left: 638px; top: 347px; font-size: 16px; color: var(--white); }
  .slide-btn { top: 381px; width: 33px; height: 32px; background: var(--teal); display: flex; align-items: center; justify-content: center; }

  .connect { left: 0; top: 478px; width: 970px; height: 87px; background: var(--sky); }
  .connect h2 { left: 139px; top: 496px; font-size: 19px; font-weight: 400; color: var(--white); }
  .connect-copy { left: 139px; top: 522px; width: 530px; font-size: 8.8px; font-style: italic; line-height: 15px; color: var(--white); }
  .btn-light { left: 674px; top: 508px; width: 157px; height: 36px; background: linear-gradient(#fafafa, #dcdcdc); border-radius: 3px; color: #666; font-size: 12px; display: flex; align-items: center; justify-content: center; box-shadow: 0 1px 2px rgba(0,0,0,.2); }

  .feature h3 { font-size: 14.5px; font-weight: 700; color: var(--ink); text-transform: uppercase; position: absolute; top: 598px; }
  .feature-photo { position: absolute; top: 628px; width: 216px; height: 128px; }
  .feature-body { position: absolute; top: 756px; width: 216px; height: 122px; background: var(--panel); border-bottom: 2px solid var(--sky); font-size: 8.6px; line-height: 17.4px; text-align: center; padding: 16px 16px 0; }

  .about-photo { left: 138px; top: 918px; width: 229px; height: 160px; background: linear-gradient(100deg, #3a3229, #6b685a 45%, #3e4c55); }
  .about h2 { left: 399px; top: 916px; font-size: 14.5px; font-weight: 700; color: var(--ink); text-transform: uppercase; }
  .about-copy { left: 399px; top: 942px; width: 432px; font-size: 8.6px; line-height: 17.4px; }
  .btn-primary { left: 399px; top: 1041px; width: 202px; height: 34px; background: var(--sky); border: 1px solid var(--sky-dark); border-radius: 2px; color: var(--white); font-size: 11.5px; font-weight: 700; display: flex; align-items: center; justify-content: center; text-transform: uppercase; }

  .site-footer { left: 0; top: 1120px; width: 970px; height: 80px; background: var(--footer); }
  .footer-link { top: 1143px; font-size: 8.6px; color: var(--white); }
  .copyright { left: 140px; top: 1166px; font-size: 8.6px; color: var(--white); }
  .follow { left: 680px; top: 1156px; font-size: 8.6px; color: var(--white); }
  .social { top: 1150px; width: 22px; height: 22px; border-radius: 50%; background: #7a8797; }
</style>
</head>
<body>
  <header>
    <div class="abs site-header"></div>
    <div class="abs header-rule"></div>
    <div class="abs brand-plate"></div>
    <div class="abs brand"><span class="brand-mark"></span><span class="brand-name">Cedar Hollow</span></div>
    <nav>
      <span class="abs main-nav" style="left:328px">Home</span>
      <span class="abs main-nav" style="left:393px">About</span>
      <span class="abs main-nav" style="left:463px">Fly Shop</span>
      <span class="abs main-nav" style="left:548px">Guide Service</span>
      <span class="abs main-nav" style="left:662px">Missouri River</span>
      <span class="abs main-nav" style="left:782px">Contact</span>
    </nav>
  </header>

  <section>
    <div class="abs hero" role="img" aria-label="Two fly fishing guides in a drift boat on the river with rocky hills behind"></div>
    <h1 class="abs hero-title">Cedar<br>Hollow</h1>
    <p class="abs hero-tag" style="top:292px">We are fly fishing shop</p>
    <p class="abs hero-tag" style="top:316px">and also provide guide service.</p>
    <p class="abs hero-sub">Guided Trips, Fly Shop, Missouri River</p>
    <div class="abs slide-btn" style="left:641px"><svg width="10" height="16" viewBox="0 0 10 16"><path d="M8 1 1 8l7 7" fill="none" stroke="#bfe3ea" stroke-width="1.5"/></svg></div>
    <div class="abs slide-btn" style="left:675px"><svg width="10" height="16" viewBox="0 0 10 16"><path d="M2 1l7 7-7 7" fill="none" stroke="#bfe3ea" stroke-width="1.5"/></svg></div>
  </section>

  <section>
    <div class="abs connect"></div>
    <div class="connect"><h2 class="abs">CONNECT WITH US</h2></div>
    <p class="abs connect-copy">Many desktop publishing packages and web page editors now use Lorem Ipsum as their default model text, and a search for 'lorem ipsum' will uncover many web sites still in their infancy. Various versions have evolved over the years, sometimes by accident,</p>
    <div class="abs btn-light">CONNECT NOW</div>
  </section>

  <section>
    <div class="feature">
      <h3 style="left:138px">Guided Trips</h3>
      <div class="feature-photo" style="left:138px;background:linear-gradient(#7fa3b4,#8aa4ae 55%,#6f8c96)" role="img" aria-label="Guide service building with a drift boat parked outside"></div>
      <svg class="abs" style="left:233px;top:680px" width="25" height="25" viewBox="0 0 25 25"><circle cx="12.5" cy="12.5" r="12.5" fill="#e8eef0" opacity=".85"/><path d="M9 14l5-5M8 12l-1.5 1.5a2.5 2.5 0 0 0 3.5 3.5L11.5 15.5M13.5 9.5 15 8a2.5 2.5 0 0 1 3.5 3.5L17 13" fill="none" stroke="#555" stroke-width="1.5"/></svg>
      <p class="feature-body" style="left:138px">Many desktop publishing packages and web page editors now use Lorem Ipsum as their default model text, and a search for 'lorem ipsum' will uncover many web sites still in their infancy. Various versions have evolved...</p>
    </div>
    <div class="feature">
      <h3 style="left:378px">Fly Shop</h3>
      <div class="feature-photo" style="left:378px;background:linear-gradient(#6f8a7e,#9c7a45 55%,#5d4a32)" role="img" aria-label="Interior of the fly shop with display racks and tables"></div>
      <p class="feature-body" style="left:378px">Many desktop publishing packages and web page editors now use Lorem Ipsum as their default model text, and a search for 'lorem ipsum' will uncover many web sites still in their infancy. Various versions have evolved...</p>
    </div>
    <div class="feature">
      <h3 style="left:616px">Missouri River</h3>
      <div class="feature-photo" style="left:616px;background:linear-gradient(#8fa4bd,#6a6a4c 40%,#9a6a45 60%,#283c4c)" role="img" aria-label="River with autumn brush and rocky hillside"></div>
      <p class="feature-body" style="left:616px">Many desktop publishing packages and web page editors now use Lorem Ipsum as their default model text, and a search for 'lorem ipsum' will uncover many web sites still in their infancy. Various versions have evolved...</p>
    </div>
  </section>

  <section class="about">
    <div class="abs about-photo" role="img" aria-label="Two guides seated in a boat on the river"></div>
    <h2 class="abs">About Cedar Hollow</h2>
    <p class="abs about-copy">It is a long established fact that a reader will be distracted by the readable content of a page when looking at its layout. The point of using Lorem Ipsum is that it has a more-or-less normal distribution of letters, as opposed to using 'Content here, content here', making it look like readable English. Many desktop publishing packages and web page editors now use Lorem Ipsum as their default model text, and a search for 'lorem ipsum' will uncover many web sites still in their infancy. Various versions have evolved over the years...</p>
    <div class="abs btn-primary">Click here for more info</div>
  </section>

  <footer>
    <div class="abs site-footer"></div>
    <span class="abs footer-link" style="left:140px">Home</span>
    <span class="abs footer-link" style="left:192px">About</span>
    <span class="abs footer-link" style="left:244px">Fly shop</span>
    <span class="abs footer-link" style="left:305px">guide service</span>
    <span class="abs footer-link" style="left:384px">Missouri river</span>
    <span class="abs footer-link" style="left:463px">Contact</span>
    <p class="abs copyright">Copyright ©. 2014. Cedar Hollow. All rights reserved.</p>
    <span class="abs follow">Follow Us :</span>
    <span class="abs social" style="left:724px"></span>
    <span class="abs social" style="left:752px"></span>
    <span class="abs social" style="left:780px"></span>
    <span class="abs social" style="left:807px"></span>
  </footer>
</body>
</html>
```